Wine label

I'm wanting to create a wine label that is very very simple, but eye catching. Jump off the shelf.

Name of Winery : Morrow Ridge

Nothing on the front but that - will be putting other info on back - which will be the brand label.

I was thinking of something MR - possibly - with morrow ridge intertwined. -

1 color label and possible 1 or 2 ink

```html
<!DOCTYPE html>
<html lang="en">
<head>
<meta charset="utf-8">
<title>Morrow Ridge — wine label options</title>
<link rel="stylesheet" href="https://fonts.googleapis.com/css2?family=Barlow+Condensed:wght@500;600&family=Barlow+Semi+Condensed:wght@500;600&display=swap">
<style>
  :root {
    --board: #d8d8d8;
    --caption: #ffffff;
    --night: #000000;
    --paper: #ffffff;
    --sky: #1ba8de;
    --signal: #e42b24;
    --ink-dark: #111111;
  }
  html, body {
    margin: 0;
    padding: 0;
    overflow: hidden;
  }
  .board {
    position: relative;
    width: 1200px;
    height: 1000px;
    background: var(--board);
    overflow: hidden;
    font-family: "Barlow Semi Condensed", "Barlow Condensed", sans-serif;
  }
  .option-caption {
    position: absolute;
    top: 22px;
    margin: 0;
    font-family: "Barlow Condensed", sans-serif;
    font-weight: 600;
    font-size: 34px;
    line-height: 1;
    color: var(--caption);
  }
  .option-caption--left { left: 32px; }
  .option-caption--right { right: 26px; }

  .label {
    position: absolute;
    width: 573px;
    height: 860px;
    box-shadow: 0 0 3px rgba(0,0,0,0.25);
  }
  .label--night { left: 18px; top: 112px; background: var(--night); }
  .label--paper { left: 608px; top: 110px; background: var(--paper); }

  .label__field {
    position: absolute;
    left: 43px;
    top: 185px;
    width: 489px;
    height: 490px;
    display: flex;
    align-items: center;
    justify-content: center;
  }
  .label--night .label__field { background: var(--sky); }
  .label--paper .label__field { background: var(--signal); }

  .label__monogram {
    font-family: "Barlow Semi Condensed", sans-serif;
    font-weight: 600;
    font-size: 170px;
    line-height: 1;
    letter-spacing: 0.02em;
  }
  .label--night .label__monogram { color: var(--paper); }
  .label--paper .label__monogram { color: var(--ink-dark); }

  .label__rule {
    position: absolute;
    left: 0;
    right: 0;
    top: 716px;
    height: 1px;
    opacity: 0.55;
  }
  .label--night .label__rule { background: var(--sky); }
  .label--paper .label__rule { background: var(--signal); }

  .label__name {
    position: absolute;
    left: 0;
    right: 0;
    top: 696px;
    margin: 0;
    text-align: center;
    font-family: "Barlow Semi Condensed", sans-serif;
    font-weight: 500;
    font-size: 33px;
    line-height: 40px;
    letter-spacing: 0.95em;
    padding-left: 0.95em;
  }
  .label--night .label__name { color: var(--sky); }
  .label--paper .label__name { color: var(--signal); }
</style>
</head>
<body>
  <main class="board">
    <p class="option-caption option-caption--left">option 3</p>
    <p class="option-caption option-caption--right">option 4</p>

    <section class="label label--night" aria-label="Label option 3">
      <div class="label__field">
        <span class="label__monogram">MR</span>
      </div>
      <div class="label__rule"></div>
      <h2 class="label__name">Morrow Ridge</h2>
    </section>

    <section class="label label--paper" aria-label="Label option 4">
      <div class="label__field">
        <span class="label__monogram">MR</span>
      </div>
      <div class="label__rule"></div>
      <h2 class="label__name">Morrow Ridge</h2>
    </section>
  </main>
</body>
</html>
```